Brivora Australia Company Values.

We have just completed our company purpose, beliefs and values (for the first time, we have not had these before)
We are now wanting to add images to each company value as a visual
so they are easily identified and understood for all our staff - we need them to remember the 5 Values.
We are a manufacturer of dental materials and infection control products, based in Melbourne.

What we would like:
- A Poster (that can be placed in our staff lunch rooms)
- The values to be lined up Horizontally
- Image on the top of the words
- Wording does not all need to be the same text font
- No image photographs - please use image graphics
- No images with people
- No dental related graphics

Target audience: Brivora staff

Our Values are:
Think Big
Have a go, learn and adapt
If you're gonna do it, do it bloody well
Empower Others
Be a good human

I have uploaded some examples.

Target Market(s)

Brivora Team members

Industry/Entity Type

Healthcare

Colors

Designer to choose colors to be used in the design.

Requirements
Must have
• Clear horizontal layout, space between each value
Should not have
• No images with humans or dental

```html
<!DOCTYPE html>
<html lang="en">
<head>
<meta charset="utf-8">
<title>Brivora Australia – Company Values</title>
<link rel="stylesheet" href="https://fonts.googleapis.com/css2?family=Barlow:wght@600;700&family=Barlow+Condensed:wght@600&family=Kaushan+Script&display=swap">
<style>
  :root {
    --canvas: #f2f2f2;
    --ink: #ffffff;
    --think-big: #f288b5;
    --learn-adapt: #3bc3d9;
    --do-it-well: #8dc63f;
    --empower: #3d95d3;
    --good-human: #f48480;
  }
  * { margin: 0; padding: 0; box-sizing: border-box; }
  html, body { width: 1200px; height: 927px; overflow: hidden; }
  body { background: var(--canvas); position: relative; font-family: "Barlow", Arial, sans-serif; color: var(--ink); }

  .values-poster { position: absolute; left: 97px; top: 227px; display: flex; gap: 8.5px; }
  .value-card { position: relative; width: 197px; height: 413px; text-align: center; }
  .value-card--think-big { background: var(--think-big); }
  .value-card--learn-adapt { background: var(--learn-adapt); }
  .value-card--do-it-well { background: var(--do-it-well); }
  .value-card--empower { background: var(--empower); }
  .value-card--good-human { background: var(--good-human); }

  .value-icon { position: absolute; left: 48px; top: 36px; width: 100px; height: 100px; fill: var(--ink); }
  .value-text { position: absolute; left: 0; right: 0; }
  .value-text span { display: block; font-weight: 700; }
  .value-text .small { font-size: 21px; line-height: 26px; }
  .value-text .tiny { font-size: 16.5px; line-height: 21px; }
  .value-text .huge { font-size: 80px; line-height: 72px; letter-spacing: 1px; }
  .value-text .condensed { font-family: "Barlow Condensed", "Arial Narrow", sans-serif; font-weight: 600; font-size: 78px; line-height: 70px; }
  .value-text .do-it { font-size: 58px; line-height: 60px; }
  .value-text .script { font-family: "Kaushan Script", cursive; font-weight: 400; font-size: 44px; line-height: 50px; }
  .value-text .others { font-size: 38px; line-height: 42px; }
  .value-text .good { font-size: 54px; line-height: 44px; }

  .value-wave { position: absolute; left: 55px; top: 370px; width: 87px; height: 12px; fill: none; stroke: var(--ink); stroke-width: 2.2; }
</style>
</head>
<body>
<main class="values-poster">

  <section class="value-card value-card--think-big">
    <svg class="value-icon" viewBox="0 0 100 100" aria-hidden="true">
      <path d="M50 22c-17 0-28 13-28 27 0 10 5 16 10 21 3 3 4 6 4 10h28c0-4 1-7 4-10 5-5 10-11 10-21 0-14-11-27-28-27z"/>
      <rect x="37" y="85" width="26" height="8" rx="1"/>
      <g stroke="#fff" stroke-width="6" stroke-linecap="round">
        <line x1="50" y1="3" x2="50" y2="10"/><line x1="27" y1="9" x2="31" y2="15"/><line x1="73" y1="9" x2="69" y2="15"/>
        <line x1="7" y1="29" x2="14" y2="32"/><line x1="93" y1="29" x2="86" y2="32"/>
      </g>
    </svg>
    <h2 class="value-text" style="top:201px"><span class="small">Think</span><span class="huge">BIG</span></h2>
    <svg class="value-wave" viewBox="0 0 87 12" aria-hidden="true"><path d="M1 6q4.5-5 9 0t9 0 9 0 9 0 9 0 9 0 9 0 9 0 9 0 4 0"/></svg>
  </section>

  <section class="value-card value-card--learn-adapt">
    <svg class="value-icon" viewBox="0 0 100 100" aria-hidden="true">
      <path d="M92 8 10 40l36 7 7 37z" stroke="#fff" stroke-width="4" stroke-linejoin="round"/>
    </svg>
    <h2 class="value-text" style="top:195px"><span class="small">Have A Go,</span><span class="condensed">LEARN</span><span class="small">And Adapt</span></h2>
    <svg class="value-wave" viewBox="0 0 87 12" aria-hidden="true"><path d="M1 6q4.5-5 9 0t9 0 9 0 9 0 9 0 9 0 9 0 9 0 9 0 4 0"/></svg>
  </section>

  <section class="value-card value-card--do-it-well">
    <svg class="value-icon" viewBox="0 0 100 100" aria-hidden="true">
      <path d="M50 10 61 36 89 38 68 56 75 84 50 69 25 84 32 56 11 38 39 36z" stroke="#fff" stroke-width="8" stroke-linejoin="round"/>
    </svg>
    <h2 class="value-text" style="top:199px"><span class="tiny">If You're</span><span class="tiny">Gonna Do It,</span><span class="do-it">DO IT</span><span class="tiny">Bloody Well</span></h2>
    <svg class="value-wave" viewBox="0 0 87 12" aria-hidden="true"><path d="M1 6q4.5-5 9 0t9 0 9 0 9 0 9 0 9 0 9 0 9 0 9 0 4 0"/></svg>
  </section>

  <section class="value-card value-card--empower">
    <svg class="value-icon" viewBox="0 0 100 100" aria-hidden="true">
      <rect x="10" y="46" width="16" height="42" rx="3"/>
      <path d="M31 46l12-18c3-5 4-10 4-16 0-4 8-4 10 2 2 7 0 14-3 22h26c6 0 9 5 8 10l-6 35c-1 5-5 7-10 7H31z"/>
    </svg>
    <h2 class="value-text" style="top:200px"><span class="script">Empower</span><span class="others">OTHERS</span></h2>
    <svg class="value-wave" viewBox="0 0 87 12" aria-hidden="true"><path d="M1 6q4.5-5 9 0t9 0 9 0 9 0 9 0 9 0 9 0 9 0 9 0 4 0"/></svg>
  </section>

  <section class="value-card value-card--good-human">
    <svg class="value-icon" viewBox="0 0 100 100" aria-hidden="true">
      <path d="M50 92 12 52C0 39 4 16 22 12c12-3 22 4 28 13 6-9 16-16 28-13 18 4 22 27 10 40z"/>
    </svg>
    <h2 class="value-text" style="top:218px"><span class="tiny">Be A</span><span class="good">Good</span><span class="tiny" style="margin-top:4px">Human</span></h2>
    <svg class="value-wave" viewBox="0 0 87 12" aria-hidden="true"><path d="M1 6q4.5-5 9 0t9 0 9 0 9 0 9 0 9 0 9 0 9 0 9 0 4 0"/></svg>
  </section>

</main>
</body>
</html>
```